Food product label for new company

2 x 4 label, red or burgundy color background, would like to take same label design and be able to change colors for product variations,
Briskwell Roasted Pecan Butter
All natural, no sugar added, non-GMO, Gluten Free, No Preservatives, Low glycemic index
10oz, produced by Briskwell Foods, Johnstown, PA
Ingredients: Toasted Pecans
Instructions: Stir and Enjoy!
Cannot use Organic until certified to be or

```html
<!DOCTYPE html>
<html lang="en">
<head>
<meta charset="utf-8">
<title>Briskwell Roasted Pecan Butter – Label</title>
<link rel="stylesheet" href="https://fonts.googleapis.com/css2?family=Luckiest+Guy&family=Patrick+Hand&display=swap">
<style>
  :root {
    --page-bg: #e9e9e7;
    --label-burgundy: #7a1f2b;
    --label-burgundy-light: #8f2d3a;
    --ribbon-cream: #f1e3cc;
    --ink-cream: #fbf3e6;
    --ink-burgundy: #4a0f18;
    --pecan-tan: #b9804d;
    --pecan-brown: #8a5a35;
  }
  * { box-sizing: border-box; margin: 0; padding: 0; }
  html, body { width: 916px; height: 1200px; overflow: hidden; }
  body {
    background: var(--page-bg);
    display: flex; align-items: center; justify-content: center;
    font-family: "Patrick Hand", sans-serif;
  }
  .label {
    position: relative;
    width: 860px; height: 620px;
    background: var(--label-burgundy);
    overflow: hidden;
  }
  .label__decor {
    position: absolute; inset: 0;
    background: radial-gradient(circle at 12% 14%, var(--label-burgundy-light) 0, transparent 28%),
                radial-gradient(circle at 90% 30%, var(--label-burgundy-light) 0, transparent 24%);
  }
  .pecans {
    position: absolute;
    background: linear-gradient(160deg, var(--pecan-tan), var(--pecan-brown));
    border-radius: 36px;
  }
  .pecans--top { left: 355px; top: 22px; width: 150px; height: 54px; }
  .pecans--left { left: 72px; top: 120px; width: 84px; height: 230px; }
  .pecans--right { right: 72px; top: 120px; width: 84px; height: 230px; }
  .pecans--bottom-left { left: 72px; top: 400px; width: 84px; height: 90px; }
  .pecans--bottom-right { right: 72px; top: 400px; width: 84px; height: 90px; }

  .display {
    font-family: "Luckiest Guy", Impact, sans-serif;
    font-weight: 400;
    text-align: center;
    position: absolute; left: 180px; right: 180px;
    line-height: 1;
  }
  .brand { top: 96px; font-size: 78px; color: var(--ink-cream); letter-spacing: 1px; }
  .variety { top: 196px; font-size: 50px; color: var(--ink-cream); }

  .ribbon {
    position: absolute; left: 180px; top: 268px;
    width: 500px; height: 86px;
    background: var(--ribbon-cream);
    border-top: 4px solid var(--ink-burgundy);
    border-bottom: 4px solid var(--ink-burgundy);
  }
  .product-name {
    position: absolute; left: 180px; width: 500px; top: 268px;
    height: 86px; line-height: 86px;
    text-align: center;
    font-family: "Luckiest Guy", Impact, sans-serif;
    font-weight: 400;
    font-size: 50px;
    color: var(--ink-burgundy);
    letter-spacing: 2px;
  }
  .claims {
    position: absolute; left: 180px; right: 180px; top: 394px;
    text-align: center;
    font-size: 25px; color: var(--ink-cream);
    letter-spacing: 1px;
  }
  .net-weight {
    position: absolute; left: 180px; right: 180px; top: 448px;
    text-align: center;
    font-family: "Luckiest Guy", Impact, sans-serif;
    font-size: 38px; color: var(--ink-cream);
    letter-spacing: 1px;
  }
  .side-panel {
    position: absolute; top: 110px; height: 400px;
    writing-mode: vertical-rl;
    font-size: 17px; line-height: 1.2;
    color: var(--ink-cream);
    text-align: center;
  }
  .side-panel--left { left: 16px; transform: rotate(180deg); }
  .side-panel--right { right: 16px; }
</style>
</head>
<body>
  <main class="label">
    <div class="label__decor" role="img" aria-label="Faint hand-drawn sun rays and swirls"></div>

    <div class="pecans pecans--top" role="img" aria-label="Illustrated pecan halves"></div>
    <div class="pecans pecans--left" role="img" aria-label="Illustrated pecan halves"></div>
    <div class="pecans pecans--right" role="img" aria-label="Illustrated pecan halves"></div>
    <div class="pecans pecans--bottom-left" role="img" aria-label="Illustrated pecan halves"></div>
    <div class="pecans pecans--bottom-right" role="img" aria-label="Illustrated pecan halves"></div>

    <h1 class="display brand">BRISKWELL</h1>
    <p class="display variety">ROASTED</p>

    <div class="ribbon" aria-hidden="true"></div>
    <h2 class="product-name">PECAN BUTTER</h2>

    <p class="claims">NON-GMO | GLUTEN FREE | NO PRESERVATIVES</p>
    <p class="net-weight">NET WT 10 OZ</p>

    <div class="side-panel side-panel--left">
      <p>All Natural | No Sugar Added</p>
      <p>Low Glycemic Index</p>
    </div>
    <div class="side-panel side-panel--right">
      <p>Ingredients: Toasted Pecans</p>
      <p>Briskwell Foods, Johnstown, PA</p>
    </div>
  </main>
</body>
</html>
```